Video Company Business Card Design

We are looking for a new design for business cards that will complement our new logo and new website design.

Target Market(s)

professionals who need video work done

Industry/Entity Type

Business

Requirements
Must have
• Logo
compliment website look seen here...http://k7studiowerks.com/brightlens/

info for card:
Derek Halloway
Producer/ Cinematographer

462 Pendlemoor SW
Alder Falls, MI 49867
(inside The VARN Center)
(555) 555-0174
Derek@brightlensfilms.com
www.brightlensfilms.com

```html
<!DOCTYPE html>
<html lang="en">
<head>
<meta charset="utf-8">
<title>Bright Lens Films – Business Card</title>
<link href="https://fonts.googleapis.com/css2?family=Mulish:wght@300;400;600;900&display=swap" rel="stylesheet">
<style>
  :root {
    --backdrop: #ececec;
    --teal-top: #37565b;
    --teal-bottom: #1f3a3d;
    --rule-light: #e6eceb;
    --band: #ffffff;
    --grey-top: #4b4b4b;
    --grey-bottom: #373737;
    --green: #1d9a3e;
    --accent-green: #5fb52f;
    --ink: #111111;
    --light: #f2f2f2;
  }
  html, body {
    margin: 0;
    width: 1200px;
    height: 1000px;
    overflow: hidden;
    background: var(--backdrop);
    font-family: "Mulish", sans-serif;
  }
  .card {
    position: absolute;
    left: 140px;
    top: 235px;
    width: 920px;
    height: 530px;
    overflow: hidden;
  }
  .card__header {
    position: absolute;
    left: 0; top: 0;
    width: 100%;
    height: 272px;
    background: linear-gradient(to bottom, var(--teal-top), var(--teal-bottom));
  }
  .card__rule {
    position: absolute;
    left: 0;
    width: 100%;
    height: 2px;
    background: var(--rule-light);
  }
  .card__rule--upper { top: 259px; }
  .card__rule--lower { top: 266px; }
  .brand {
    position: absolute;
    left: 0; right: 0;
    top: 163px;
    display: flex;
    justify-content: center;
    align-items: center;
    gap: 14px;
  }
  .brand__name {
    font-weight: 600;
    font-size: 66px;
    line-height: 1;
    letter-spacing: 0.5px;
    color: var(--light);
  }
  .brand__mark {
    width: 46px;
    height: 46px;
    background: var(--accent-green);
    border-radius: 4px;
  }
  .card__nameband {
    position: absolute;
    left: 0; top: 272px;
    width: 100%;
    height: 79px;
    background: var(--band);
  }
  .person {
    position: absolute;
    left: 52px;
    top: 25px;
    margin: 0;
    white-space: nowrap;
  }
  .person__name {
    font-weight: 900;
    font-size: 35px;
    color: var(--ink);
    letter-spacing: 0.3px;
  }
  .person__role {
    font-weight: 400;
    font-size: 25px;
    color: var(--green);
    margin-left: 6px;
  }
  .card__footer {
    position: absolute;
    left: 0; top: 351px;
    width: 100%;
    height: 179px;
    background: linear-gradient(to bottom, var(--grey-top), var(--grey-bottom));
    color: var(--light);
    font-weight: 300;
    font-size: 21px;
    line-height: 30px;
  }
  .address {
    position: absolute;
    left: 52px;
    top: 44px;
    font-style: normal;
  }
  .contacts {
    position: absolute;
    left: 555px;
    top: 44px;
    margin: 0;
    padding: 0;
    list-style: none;
  }
  .contacts li {
    display: flex;
    align-items: center;
    gap: 10px;
  }
  .contacts svg {
    width: 22px;
    height: 22px;
    flex: none;
  }
</style>
</head>
<body>
  <div class="card">
    <header class="card__header">
      <div class="brand">
        <span class="brand__name">BRIGHTLENSFILMS</span>
        <span class="brand__mark"></span>
      </div>
      <div class="card__rule card__rule--upper"></div>
      <div class="card__rule card__rule--lower"></div>
    </header>
    <div class="card__nameband">
      <p class="person">
        <span class="person__name">DEREK HALLOWAY</span>
        <span class="person__role">Producer/ Cinematographer</span>
      </p>
    </div>
    <footer class="card__footer">
      <address class="address">
        462 Pendlemoor SW<br>
        Alder Falls, MI 49867<br>
        (inside The VARN Center)
      </address>
      <ul class="contacts">
        <li>
          <svg viewBox="0 0 22 22" aria-hidden="true"><path d="M6 3c-2 1-3 3-3 8s1 7 3 8l3-1-1-5 2-1V10L8 9l1-5z" fill="#f2f2f2"/><path d="M12 4v14" stroke="#f2f2f2" stroke-width="2"/></svg>
          (555) 555-0174
        </li>
        <li>
          <svg viewBox="0 0 22 22" aria-hidden="true"><rect x="2" y="5" width="18" height="13" rx="2" fill="none" stroke="#f2f2f2" stroke-width="2"/><path d="M3 6l8 6 8-6" fill="none" stroke="#f2f2f2" stroke-width="2"/></svg>
          Derek@brightlensfilms.com
        </li>
        <li>
          <svg viewBox="0 0 22 22" aria-hidden="true"><circle cx="11" cy="11" r="9" fill="none" stroke="#f2f2f2" stroke-width="2"/><path d="M2 11h18M11 2c-4 5-4 13 0 18M11 2c4 5 4 13 0 18" fill="none" stroke="#f2f2f2" stroke-width="1.6"/></svg>
          www.brightlensfilms.com
        </li>
      </ul>
    </footer>
  </div>
</body>
</html>
```